BrXpertz Business Cards for SME Experts

We need a business card for a new company based in Clearwater FL called Kestrel of Merit. KoM is your access to on-demand subject matter experts. The final design should be very clean communicating innovation and expertise. Our logo design is attached.

The Information Age has affected the workforce in that automation and computerization have resulted in higher productivity coupled with net job loss of many knowledgeable employees. Combined with the creation of the internet and search capabilities, the disintermediation of the value chain of Subject Matter Experts (SME) has happened. We no longer need to work through traditional consulting firms for all consulting needs, instead the direct access to the SME, through a leaner and lower cost model is what the market is demanding.
BrXpertz is a new marketplace to buy consulting services. The business model is that all consultants (subject matter experts) can become a consulting resource in the marketplace following our guidelines. The consumer can now easily access consultants that they could not find easily before.
In much the way an Zyla car can be identified and requested, so can a BrXpertz Consultant. Each consultant can be identified by: location, expertise, billing rate, and prior experience rating.
By seamlessly connecting consultants to requesters through a new Kestrel of Merit marketplace, you now will have an easy to use and quicker turnaround to request and staff your consulting needs. Leveraging the KoM app, you can access the subject matter expert you need for your business requirement.

Target Market(s)

Small and medium sized companies; non-profits

Industry/Entity Type

Business Consultant

Contact Information for Business Card

Name
website
email address
Logo
mailing address (debating if I really need...)
twitter
LinkedIn

Requirements
Must have
• the logo I have included in the design; want the colors to be consistent with the logo design

```html
<!DOCTYPE html>
<html lang="en">
<head>
<meta charset="UTF-8">
<title>Kestrel of Merit – Business Card</title>
<link rel="stylesheet" href="https://fonts.googleapis.com/css2?family=Nunito:wght@400;600;700;800&display=swap">
<style>
  :root {
    --page-bg: #e4e6ea;
    --card-top: #f4f6f8;
    --card-bottom: #e7eaee;
    --teal: #1f8ea0;
    --navy: #1a1d4a;
    --ink: #2b2e55;
    --blush: #e6c7c9;
    --gold: #cbb28d;
    --white: #ffffff;
  }
  * { margin: 0; padding: 0; box-sizing: border-box; }
  html, body {
    width: 1200px;
    height: 970px;
    overflow: hidden;
    background: var(--page-bg);
    font-family: "Nunito", sans-serif;
  }
  .card {
    position: absolute;
    left: 80px;
    top: 189px;
    width: 1040px;
    height: 592px;
    background: linear-gradient(180deg, var(--card-top), var(--card-bottom));
    box-shadow: 0 18px 40px rgba(20, 24, 60, 0.18);
    overflow: hidden;
  }
  .card-waves {
    position: absolute;
    left: 0;
    top: 0;
    width: 1040px;
    height: 592px;
  }
  .identity {
    position: absolute;
    left: 70px;
    top: 90px;
  }
  .identity-name {
    font-size: 36px;
    font-weight: 700;
    color: var(--teal);
    line-height: 1.05;
    letter-spacing: 0.5px;
  }
  .identity-role {
    font-size: 29px;
    font-weight: 400;
    color: var(--ink);
    line-height: 1.05;
    letter-spacing: 1px;
  }
  .address {
    position: absolute;
    left: 70px;
    top: 224px;
    font-size: 30px;
    color: var(--ink);
    line-height: 1.15;
    letter-spacing: 0.6px;
    font-style: normal;
  }
  .contacts {
    position: absolute;
    left: 70px;
    top: 328px;
    list-style: none;
  }
  .contact-line {
    display: flex;
    align-items: center;
    gap: 8px;
    font-size: 29px;
    color: var(--ink);
    line-height: 32px;
    letter-spacing: 0.6px;
  }
  .contact-icon {
    width: 28px;
    height: 28px;
    flex: none;
  }
  .brand-mark {
    position: absolute;
    left: 572px;
    top: 112px;
    width: 408px;
    display: flex;
    align-items: center;
    justify-content: center;
    gap: 14px;
  }
  .brand-mark-dot {
    width: 36px;
    height: 36px;
    border-radius: 50%;
    background: var(--teal);
  }
  .brand-mark-name {
    font-size: 60px;
    font-weight: 800;
    color: var(--navy);
    line-height: 1;
  }
  .brand {
    position: absolute;
    left: 552px;
    top: 236px;
    width: 448px;
    text-align: center;
    font-size: 50px;
    font-weight: 800;
    color: var(--navy);
    letter-spacing: 0.3px;
    line-height: 1.2;
  }
  .website {
    position: absolute;
    right: 62px;
    top: 510px;
    font-size: 28px;
    color: var(--gold);
    letter-spacing: 0.8px;
  }
</style>
</head>
<body>
  <main class="card">
    <svg class="card-waves" viewBox="0 0 1040 592" aria-hidden="true">
      <path d="M0 380 C 80 400, 170 460, 330 475 C 560 495, 800 430, 1040 488 L 1040 592 L 0 592 Z" fill="var(--blush)" opacity="0.55"/>
      <path d="M0 385 C 60 400, 120 460, 250 478 C 420 500, 700 430, 880 445 C 960 452, 1010 470, 1040 488 L 1040 492 C 1000 470, 950 458, 880 452 C 700 438, 430 505, 250 488 C 120 478, 40 470, 0 478 Z" fill="var(--teal)"/>
      <path d="M0 510 C 200 500, 420 490, 640 470 C 800 456, 940 450, 1040 492 L 1040 592 L 0 592 Z" fill="var(--navy)"/>
    </svg>

    <header class="identity">
      <h1 class="identity-name">Employee Name</h1>
      <p class="identity-role">Managing Director</p>
    </header>

    <address class="address">
      0000 your address Avenue<br>
      Marlow Falls, SD 0000
    </address>

    <ul class="contacts">
      <li class="contact-line">
        <svg class="contact-icon" viewBox="0 0 28 28" aria-label="Phone">
          <rect width="28" height="28" fill="var(--teal)"/>
          <path d="M6 11 C6 8, 22 8, 22 11 L19 13 L17 11 L11 11 L9 13 Z" fill="var(--white)"/>
          <rect x="8" y="14" width="12" height="8" rx="1" fill="var(--white)"/>
        </svg>
        <span>000-111-0000</span>
      </li>
      <li class="contact-line">
        <svg class="contact-icon" viewBox="0 0 28 28" aria-label="Email">
          <rect width="28" height="28" fill="var(--teal)"/>
          <rect x="5" y="8" width="18" height="13" fill="none" stroke="var(--white)" stroke-width="2"/>
          <path d="M5 8 L14 16 L23 8 M5 21 L12 14 M23 21 L16 14" fill="none" stroke="var(--white)" stroke-width="1.6"/>
        </svg>
        <span>abc@yourmail.com</span>
      </li>
    </ul>

    <div class="brand-mark" aria-label="KoM logo">
      <span class="brand-mark-dot"></span>
      <span class="brand-mark-name">KoM</span>
    </div>

    <p class="brand">Kestrel of Merit</p>

    <p class="website">www.abcyourweb.com</p>
  </main>
</body>
</html>
```